Kestrel Summit 2019 Enemies of the End-Times Church Flyer

We want a church conference flyer designed. We are looking for a professional, yet catchy design that uses our brand colors and logo creatively while communicating key information of the event effectively. <br/>The flyer must include all of the following:<br/>Title: Kestrel Summit 2019<br/>Topic: The Enemies of The End-Times Church <br/>Subtitles: <br/> -How the antichrist raises an army by social behavior engineering. <br/>-How the architects of modern social constructs escaped the church's radar. <br/>-The Holy Spirit's end-times agenda:<br/> The Knock-Out Punch!<br/>Speaker: Prophet Marcus Toliver <br/>Dates/time: December 27, 28 & 29 at 6pm<br/>Location: Halvorn Community Center <br/> 241 Pellham Street <br/> Portland, ME 04102<br/>Contact info: phone: 207-555-0148 <br/>email: contact@brookmeadow.example <br/> www.vutel.example<br/>*The flyer must also include a picture of the speaker and our Vutel logo <br/>Thanks, we look forward to seeing what you come up with!

Colors

Designer to choose colors to be used in the design.

Requirements
Must have
• The flyer must include all of the following:
• Title: Kestrel Summit 2019
• Topic: The Enemies of The End-Times Church
• Subtitles:
• -How the antichrist raises an army by social behavior engineering.
• -How the architects of modern social constructs escaped the church's radar.
• -The Holy Spirit's end-times agenda:
• The Knock-Out Punch!
• Speaker: Prophet Marcus Toliver
• Dates/time: December 27, 28 & 29 at 6pm
• Location: Halvorn Community Center
• 241 Pellham Street
• Portland, ME 04102
• Contact info: phone: 207-555-0148
• email: contact@brookmeadow.example
• www.vutel.example
• *The flyer must also include a picture of the speaker and our Vutel logo
Should not have
• Pictures of crosses or church buildings

```html
<!DOCTYPE html>
<html lang="en">
<head>
<meta charset="utf-8">
<title>Kestrel Summit 2019 Flyer</title>
<link rel="stylesheet" href="https://fonts.googleapis.com/css2?family=Oswald:wght@500;600;700&family=PT+Serif:wght@400;700&family=Roboto+Condensed:wght@400;700&family=Roboto:wght@400;500&display=swap">
<style>
  :root {
    --navy: #0f3f73;
    --navy-deep: #0b2f58;
    --blue: #1f5c9c;
    --orange: #f0962a;
    --orange-deep: #e3861a;
    --maroon: #7a1d16;
    --ink: #1b1b1b;
    --paper: #ffffff;
    --stage: #e4e4e4;
  }
  * { margin: 0; padding: 0; box-sizing: border-box; }
  html, body { width: 1200px; height: 1200px; overflow: hidden; background: var(--stage); }
  .flyer {
    position: absolute; left: 258px; top: 120px;
    width: 570px; height: 800px;
    transform: scale(1.2); transform-origin: 0 0;
    background: var(--paper); overflow: hidden;
  }
  .flyer-shapes { position: absolute; inset: 0; }
  .abs { position: absolute; }

  .brand-name { left: 38px; top: 30px; font-family: 'Oswald', sans-serif; font-weight: 600; font-size: 38px; color: var(--navy); letter-spacing: 1px; line-height: 1; }

  .site-url { left: 330px; top: 24px; font-family: 'Roboto', sans-serif; font-weight: 500; font-size: 16px; color: var(--paper); letter-spacing: .8px; }

  .event-title { left: 25px; top: 140px; width: 230px; font-family: 'Oswald', sans-serif; font-weight: 600; color: var(--navy); line-height: 1; }
  .event-title .title-main { display: block; font-size: 64px; letter-spacing: 1px; background: linear-gradient(90deg, var(--blue), var(--navy)); -webkit-background-clip: text; background-clip: text; color: transparent; }
  .event-title .title-sub { display: block; font-size: 46px; letter-spacing: 6px; margin-top: 6px; color: var(--navy); }
  .event-year { left: 263px; top: 145px; width: 35px; height: 115px; background: var(--orange); display: flex; flex-direction: column; align-items: center; justify-content: center; font-family: 'Oswald', sans-serif; font-weight: 600; font-size: 24px; color: var(--paper); line-height: 1.08; }

  .topic-column { left: 15px; top: 276px; width: 250px; text-align: center; }
  .topic-label { font-family: 'PT Serif', serif; font-size: 21px; color: var(--maroon); letter-spacing: 1px; }
  .topic-heading { margin-top: 12px; font-family: 'Oswald', sans-serif; font-weight: 600; font-size: 16px; color: var(--ink); line-height: 1.15; }
  .topic-heading .topic-emph { display: block; font-size: 22px; }
  .topic-point { margin-top: 10px; font-family: 'PT Serif', serif; font-size: 12.5px; color: var(--ink); line-height: 1.25; text-transform: uppercase; }
  .topic-rule { width: 20px; height: 2px; background: var(--ink); margin: 22px auto 0; }

  .speaker-photo { left: 0; top: 0; width: 570px; height: 800px; }
  .speaker-label { left: 300px; top: 512px; width: 230px; text-align: center; font-family: 'Roboto', sans-serif; font-size: 15px; color: #d8e4f2; letter-spacing: 2.5px; }
  .speaker-name { left: 285px; top: 537px; width: 250px; text-align: center; font-family: 'Roboto Condensed', sans-serif; font-weight: 700; font-size: 19px; color: var(--paper); }

  .agenda-kicker { left: 0; top: 590px; width: 570px; text-align: center; font-family: 'PT Serif', serif; font-size: 14px; color: var(--paper); letter-spacing: 1px; }
  .agenda-headline { left: 0; top: 606px; width: 570px; text-align: center; font-family: 'PT Serif', serif; font-weight: 700; font-size: 32px; color: var(--ink); }
  .event-dates { left: 0; top: 660px; width: 570px; text-align: center; font-family: 'Oswald', sans-serif; font-weight: 500; font-size: 22px; color: var(--maroon); letter-spacing: 1.5px; }
  .event-location { left: 0; top: 706px; width: 570px; text-align: center; font-family: 'PT Serif', serif; font-size: 15px; color: #2a1a0c; line-height: 1.3; }
  .event-location b { font-weight: 700; }
  .contact-phone, .contact-email { top: 765px; font-family: 'PT Serif', serif; font-size: 14px; color: var(--paper); white-space: nowrap; }
  .contact-phone { left: 22px; }
  .contact-email { right: 20px; }
</style>
</head>
<body>
  <main class="flyer">
    <svg class="flyer-shapes" viewBox="0 0 570 800" width="570" height="800" aria-hidden="true">
      <defs>
        <linearGradient id="orangeField" x1="0" y1="0" x2="1" y2="0">
          <stop offset="0" stop-color="#e8921c"/>
          <stop offset=".5" stop-color="#f2a846"/>
          <stop offset="1" stop-color="#e8901e"/>
        </linearGradient>
        <linearGradient id="dateBand" x1="0" y1="0" x2="1" y2="0">
          <stop offset="0" stop-color="#f2b565" stop-opacity=".6"/>
          <stop offset=".5" stop-color="#fbdcae"/>
          <stop offset="1" stop-color="#f2b565" stop-opacity=".6"/>
        </linearGradient>
        <linearGradient id="whiteField" x1="0" y1="0" x2="0" y2="1">
          <stop offset="0" stop-color="#ffffff"/>
          <stop offset="1" stop-color="#f1f1f1"/>
        </linearGradient>
      </defs>
      <rect x="0" y="460" width="570" height="340" fill="url(#orangeField)"/>
      <path d="M0 0 H570 V520 Q330 560 240 545 Q110 505 0 505 Z" fill="url(#whiteField)"/>
      <path d="M0 95 Q120 90 240 30 L570 30 L570 60 L250 60 Q140 110 0 120 Z" fill="#ececec" opacity=".7"/>
      <path d="M0 0 H245 Q215 80 0 95 Z" fill="#ffffff"/>
      <polygon points="248,17 570,17 570,50 235,50" fill="var(--navy)"/>
      <polygon points="370,122 392,122 301,360 279,360" fill="var(--navy)"/>
      <polygon points="405,95 570,95 570,540 235,540" fill="#2b2d33"/>
      <rect x="0" y="655" width="570" height="45" fill="url(#dateBand)"/>
      <rect x="0" y="755" width="570" height="36" fill="var(--navy)"/>
      <polygon points="300,505 545,505 520,580 282,580" fill="var(--navy)"/>
      <path d="M505 510 H540 L532 530" fill="none" stroke="#ffffff" stroke-width="1"/>
      <path d="M287 575 L295 555" fill="none" stroke="#ffffff" stroke-width="1"/>
    </svg>

    <svg class="abs speaker-photo" viewBox="0 0 570 800" width="570" height="800" role="img" aria-label="Portrait photograph of the speaker, Prophet Marcus Toliver, seated in front of bookshelves">
      <defs>
        <linearGradient id="photoTone" x1="0" y1="0" x2="1" y2="1">
          <stop offset="0" stop-color="#4a4c52"/>
          <stop offset=".55" stop-color="#2e3036"/>
          <stop offset="1" stop-color="#1c1d22"/>
        </linearGradient>
      </defs>
      <polygon points="408,97 570,97 570,503 250,503" fill="url(#photoTone)"/>
    </svg>

    <div class="abs brand-name">VUTEL</div>
    <div class="abs site-url">www.vutel.example</div>

    <h1 class="abs event-title"><span class="title-main">KESTREL</span><span class="title-sub">SUMMIT</span></h1>
    <div class="abs event-year"><span>2</span><span>0</span><span>1</span><span>9</span></div>

    <section class="abs topic-column">
      <div class="topic-label">- TOPIC -</div>
      <h2 class="topic-heading">THE ENEMIES OF THE END-TIMES <span class="topic-emph">CHURCH</span></h2>
      <p class="topic-point">How the antichrist raises an army by social behavior engineering.</p>
      <p class="topic-point">How the architects of modern social constructs escaped the church's radar.</p>
      <div class="topic-rule"></div>
    </section>

    <div class="abs speaker-label">- Speaker -</div>
    <div class="abs speaker-name">Prophet Marcus Toliver</div>

    <div class="abs agenda-kicker">- THE HOLY SPIRIT'S END-TIMES AGENDA -</div>
    <div class="abs agenda-headline">THE KNOCK-OUT PUNCH!</div>
    <div class="abs event-dates">DECEMBER 27, 28 &amp; 29 &nbsp;|&nbsp;AT 6PM</div>
    <div class="abs event-location"><b>Location:</b>Halvorn Community Center 241 Pellham Street<br>Portland, ME 04102</div>
    <div class="abs contact-phone">Contact us - 207-555-0148</div>
    <div class="abs contact-email">Email: contact@brookmeadow.example</div>
  </main>
</body>
</html>
```